ridge-mosaic builders & interiors

I need a web design for my company we offer counter tops. tile for floors,showers,kitchen backsplashes and more also need a place where the client
can write reviews

Industry/Entity Type

Tile

```html
<!DOCTYPE html>
<html lang="en">
<head>
<meta charset="utf-8">
<title>Ridge-Mosaic Builders &amp; Interiors</title>
<link rel="stylesheet" href="https://fonts.googleapis.com/css2?family=Roboto+Condensed:wght@400;700&family=Arimo:ital,wght@0,400;1,400&display=swap">
<style>
:root{
  --orange:#f26f1f;
  --grey-text:#777a7d;
  --body-text:#555555;
  --dark:#3a3a3a;
  --footer:#5d5d5d;
  --icon:#d6d6d6;
  --button-top:#6d727a;
  --button-bottom:#4e535b;
  --arrow-red:#c63a22;
}
*{box-sizing:border-box;margin:0;padding:0}
html,body{width:1200px;height:1120px;overflow:hidden;background:#fff}
body{font-family:"Arimo",Arial,sans-serif;color:var(--body-text)}
.page{position:relative;width:1200px;height:1120px;overflow:hidden;background:#fff}
.abs{position:absolute}
.top-bar{left:172px;top:0;width:857px;height:11px;background:var(--orange)}
.brand{left:176px;top:58px;font-family:"Roboto Condensed",sans-serif;font-weight:400;font-size:25px;line-height:33px;color:var(--orange);text-transform:uppercase;letter-spacing:0.5px;white-space:nowrap}
.social{left:680px;top:48px;display:flex;gap:3.5px}
.social span{width:21px;height:21px;border-radius:50%;background:var(--icon);display:block}
.divider{left:838px;top:38px;width:1px;height:39px;background:#dcdcdc}
.contact{left:850px;font-size:11px;color:var(--grey-text);display:flex;align-items:center;gap:8px;white-space:nowrap}
.contact.phone{top:37px}
.contact.mail{top:61px}
.nav{top:110px;font-family:"Roboto Condensed",sans-serif;font-size:14.5px;color:var(--grey-text);text-transform:uppercase;white-space:nowrap}
.nav.active{color:var(--orange)}
.hero{left:172px;top:148px;width:857px;height:375px;background:linear-gradient(160deg,#c9b27a 0%,#8a5a36 30%,#6b3f26 55%,#a57a4b 78%,#5a4a35 100%)}
.caption{left:172px;height:41px;background:rgba(30,22,18,0.78);color:#fff;font-family:"Roboto Condensed",sans-serif;font-size:19px;line-height:41px;padding:0 20px;text-transform:uppercase;white-space:nowrap}
.caption.one{top:405px}
.caption.two{top:454px}
.hero-arrow{top:490px;width:23px;height:23px;background:var(--arrow-red);display:flex;align-items:center;justify-content:center}
.welcome-title{left:172px;top:555px;width:857px;text-align:center;font-family:"Roboto Condensed",sans-serif;font-size:20.5px;color:var(--orange);text-transform:uppercase}
.welcome-text{left:195px;top:590px;width:810px;text-align:center;font-size:12.3px;line-height:20.6px;color:var(--body-text)}
.photo{top:700px;width:264px;height:139px}
.photo.vanity{left:172px;background:linear-gradient(135deg,#b8c7c4 0%,#d8c08f 40%,#3b2a24 75%,#8c5a4a 100%)}
.photo.granite{left:468px;background:linear-gradient(135deg,#7d8890 0%,#a79a86 35%,#55606a 65%,#9aa3a8 100%)}
.col-title{top:856px;font-family:"Roboto Condensed",sans-serif;font-size:18.5px;color:var(--orange);text-transform:uppercase;white-space:nowrap}
.col-text{top:889px;width:270px;font-size:9.6px;line-height:19.7px;color:var(--body-text)}
.btn{top:980px;width:103px;height:31px;border-radius:3px;background:linear-gradient(var(--button-top),var(--button-bottom));color:#fff;font-size:12px;line-height:31px;text-align:center;box-shadow:0 1px 2px rgba(0,0,0,0.35)}
.test-title{left:766px;top:696px;font-family:"Roboto Condensed",sans-serif;font-size:18.5px;color:var(--orange);text-transform:uppercase}
.test-arrows{left:1004px;top:700px;display:flex;gap:6px}
.reviewer{left:768px;top:733px;font-size:12px;color:var(--orange);white-space:nowrap}
.reviewer i{font-size:9.5px}
.reviewer .date{font-style:italic;font-size:9.5px;color:#888}
.portrait{left:767px;top:765px;width:109px;height:113px;border:1px solid #ddd;padding:2px;background:#fff}
.portrait div{width:100%;height:100%;background:linear-gradient(160deg,#eef1f3 0%,#c9d6dd 50%,#6aa9d6 100%)}
.quote{left:893px;top:760px;width:140px;font-size:9.6px;line-height:19.7px;color:var(--body-text)}
.quote-more{left:767px;top:896px;width:265px;font-size:9.6px;line-height:19.7px;color:var(--body-text)}
.footer{left:0;top:1058px;width:1200px;height:62px;background:var(--footer)}
.footer-links{left:178px;top:1082px;display:flex;font-size:11px;color:#f0f0f0;white-space:nowrap}
.footer-links span.sep{margin:0 20px}
.copyright{left:600px;top:1082px;width:428px;text-align:right;font-size:11px;color:#f0f0f0;white-space:nowrap}
</style>
</head>
<body>
<div class="page">
  <div class="abs top-bar"></div>

  <div class="abs brand">Ridge-Mosaic<br>Builders &amp; Interiors</div>

  <div class="abs social" aria-label="Social links">
    <span></span><span></span><span></span><span></span><span></span><span></span>
  </div>
  <div class="abs divider"></div>
  <div class="abs contact phone">
    <svg width="9" height="13" viewBox="0 0 9 13"><rect x="1" y="0.5" width="7" height="12" rx="1.2" fill="none" stroke="#8a8a8a" stroke-width="1.3"/><rect x="2.5" y="2.5" width="4" height="6" fill="#8a8a8a"/></svg>
    <span>( 555 ) 014 2290</span>
  </div>
  <div class="abs contact mail">
    <svg width="13" height="10" viewBox="0 0 13 10"><rect x="0.5" y="0.5" width="12" height="9" fill="#8a8a8a"/><path d="M0.5 0.5 L6.5 5.5 L12.5 0.5" fill="none" stroke="#fff" stroke-width="1"/></svg>
    <span>info@ridgemosaicbuilders.com</span>
  </div>

  <div class="abs nav active" style="left:470px">Home</div>
  <div class="abs nav" style="left:571px">About us</div>
  <div class="abs nav" style="left:693px">Servcies</div>
  <div class="abs nav" style="left:814px">Testimonials</div>
  <div class="abs nav" style="left:954px">Contact us</div>

  <div class="abs hero" role="img" aria-label="Kitchen island with rustic copper-toned stone countertop, sink and stacked stone base"></div>
  <div class="abs caption one">Ridge-Mosaic Builders Provide</div>
  <div class="abs caption two">Counter tops, tile for floors,showers,kitchen backsplashes.</div>
  <div class="abs hero-arrow" style="left:969px"><svg width="10" height="12" viewBox="0 0 10 12"><path d="M7 1 L2 6 L7 11" fill="none" stroke="#fff" stroke-width="1.5"/></svg></div>
  <div class="abs hero-arrow" style="left:993px"><svg width="10" height="12" viewBox="0 0 10 12"><path d="M3 1 L8 6 L3 11" fill="none" stroke="#fff" stroke-width="1.5"/></svg></div>

  <div class="abs welcome-title">Welcome to Ridge-Mosaic Builders</div>
  <p class="abs welcome-text">It is a long established fact that a reader will be distracted by the readable content of a page when looking at its layout. The point of using Lorem Ipsum is that it has a more-or-less normal distribution of letters, as opposed to using 'Content here, content here', making it look like readable English. Many desktop publishing packages and web page editors now use Lorem Ipsum as their default model....</p>

  <div class="abs photo vanity" role="img" aria-label="Bathroom vanity with cream stone countertop and dark wood cabinets"></div>
  <div class="abs col-title" style="left:172px">About Ridge-Mosaic Builders</div>
  <p class="abs col-text" style="left:173px">It is a long established fact that a reader will be distracted by the readable content of a page when looking at its layout. The point of using Lorem Ipsum is that it has a more-or-less normal distribution of letters, as opposed...</p>
  <div class="abs btn" style="left:172px">Read more</div>

  <div class="abs photo granite" role="img" aria-label="Large slab of veined granite standing in a stone yard"></div>
  <div class="abs col-title" style="left:468px">Our Services</div>
  <p class="abs col-text" style="left:469px">It is a long established fact that a reader will be distracted by the readable content of a page when looking at its layout. The point of using Lorem Ipsum is that it has a more-or-less normal distribution of letters, as opposed...</p>
  <div class="abs btn" style="left:467px">Read more</div>

  <div class="abs test-title">Testimonials</div>
  <div class="abs test-arrows">
    <svg width="7" height="10" viewBox="0 0 7 10"><path d="M5 1 L1.5 5 L5 9" fill="none" stroke="#999" stroke-width="1.2"/></svg>
    <svg width="7" height="10" viewBox="0 0 7 10"><path d="M2 1 L5.5 5 L2 9" fill="none" stroke="#999" stroke-width="1.2"/></svg>
  </div>
  <div class="abs reviewer">Marlon Ashby <i>( Business Man )</i> <span class="date">24 Dec 2014</span></div>
  <div class="abs portrait"><div role="img" aria-label="Portrait of the reviewer, a smiling man in a blue shirt"></div></div>
  <p class="abs quote">It is a long established fact that a reader will be distracted by the readable content of a page when looking at its layout. The point of using Lorem Ipsum is that it has a more-or-less</p>
  <p class="abs quote-more">It is a long established fact that a reader will be distracted by the readable content of a page when looking at its layout. The point of using is that it has a more-or-less...</p>
  <div class="abs btn" style="left:766px">Read more</div>

  <div class="abs footer"></div>
  <div class="abs footer-links">
    <span>Home</span><span class="sep">|</span><span>About us</span><span class="sep">|</span><span>Servcies</span><span class="sep">|</span><span>Testimonials</span><span class="sep">|</span><span>Contact us</span>
  </div>
  <div class="abs copyright">© Copyright 2014. Ridge-Mosaic Builders &amp; Interiors. All rights reserved.</div>
</div>
</body>
</html>
```